Business Card Design

We need a business card design for a Dry cleaners in Brisbane, Australia. We are trying to promote a fresh/clean image consistent with our website. www.finchlanelaundry.com.au

Looking for a professional neat card that's easy to read.

Target Market(s)

Customers looking for a professional, fresh and clean drycleaners.

Industry/Entity Type

Business

Contact Information for Business Card

See our existing business card. The Fax number (07) 3648 2051 to be removed.

Requirements
Must have
• All the details on current business card less the fax number.
Nice to have
• I like white text on coloured background. Blue works well as we are located near the water...

```html
<!DOCTYPE html>
<html lang="en">
<head>
<meta charset="utf-8">
<title>Finch Lane Laundry – Business Card</title>
<link rel="stylesheet" href="https://fonts.googleapis.com/css2?family=Josefin+Sans:wght@400;600&display=swap">
<style>
  :root {
    --ink: #1a1a1a;
    --white: #ffffff;
    --brand-blue: #2a6df0;
    --deep-blue: #0a26ff;
    --mid-blue: #2a80ff;
    --aqua: #24ccff;
    --pale-aqua: #b8ecfa;
    --mist: #eefafd;
    --band: #ccf8ff;
  }
  html, body {
    margin: 0;
    padding: 0;
    overflow: hidden;
    background: var(--white);
  }
  .card {
    position: relative;
    width: 1200px;
    height: 658px;
    overflow: hidden;
    background: var(--white);
    font-family: "Josefin Sans", "Century Gothic", sans-serif;
    font-variant: small-caps;
    color: var(--ink);
  }
  .brand {
    position: absolute;
    left: 88px;
    top: 62px;
    display: flex;
    align-items: center;
    gap: 14px;
    font-variant: normal;
    font-weight: 600;
    font-size: 32px;
    color: var(--brand-blue);
  }
  .brand-dot {
    width: 26px;
    height: 26px;
    border-radius: 50%;
    background: var(--brand-blue);
  }
  .address {
    position: absolute;
    right: 56px;
    top: 8px;
    margin: 0;
    text-align: right;
    font-style: normal;
    font-size: 34px;
    line-height: 56px;
    letter-spacing: 3px;
  }
  .feature-band {
    position: absolute;
    left: 0;
    top: 204px;
    width: 1200px;
    height: 257px;
    border-radius: 128px;
    background: linear-gradient(90deg, var(--deep-blue) 0%, var(--mid-blue) 28%, var(--aqua) 58%, var(--pale-aqua) 78%, var(--mist) 100%);
  }
  .contact {
    position: absolute;
    left: 0;
    width: 1200px;
    top: 266px;
    text-align: center;
    color: var(--white);
  }
  .contact-name {
    margin: 0;
    font-size: 44px;
    font-weight: 400;
    letter-spacing: 5px;
  }
  .contact-mobile {
    margin: 4px 0 0;
    font-size: 25px;
    letter-spacing: 3px;
  }
  .contact-email {
    margin: 12px 0 0;
    font-size: 18px;
    letter-spacing: 2.5px;
  }
  .branch-band {
    position: absolute;
    left: 4px;
    right: 4px;
    top: 583px;
    height: 10px;
    background: var(--band);
  }
  .branches {
    position: absolute;
    left: 0;
    top: 574px;
    width: 1200px;
    height: 40px;
    margin: 0;
    padding: 0;
    list-style: none;
    font-size: 30px;
    letter-spacing: 3px;
  }
  .branch { position: absolute; top: 0; }
  .branch--kestrel { left: 88px; }
  .branch--ashmore { left: 474px; }
  .branch--linden { left: 868px; }
</style>
</head>
<body>
<main class="card">
  <div class="brand"><span class="brand-dot"></span>Finch Lane Laundry</div>

  <address class="address">
    27 Marlow St<br>
    Kestrel Qld 4199<br>
    P: (07) 3581 7420
  </address>

  <div class="feature-band" role="img" aria-label="Decorative row of overlapping bubbles fading from deep blue to pale aqua"></div>

  <section class="contact">
    <h1 class="contact-name">Jordan Ellery</h1>
    <p class="contact-mobile">M: 0412 608 354</p>
    <p class="contact-email">E: jordan@finchlanelaundry.com.au</p>
  </section>

  <div class="branch-band"></div>
  <ul class="branches">
    <li class="branch branch--kestrel">*Kestrel</li>
    <li class="branch branch--ashmore">*Ashmore</li>
    <li class="branch branch--linden">*Linden Pt</li>
  </ul>
</main>
</body>
</html>
```